The Quiet Ledger Podcast Cover Art

I'm upgrading my podcast cover art to a new design. The show is called The Quiet Ledger and we interview guests who have gone through different challenges/adversities that we face in life. During the interview, we unpack how they've gotten past the adversity and how that insight might help others. I will link the show and old cover art. I will upload a new photo or two that can be used for the new cover art.

Look at previous cover for items that needed on the cover like Itunes, spotify etc.

Should also have a small caption that states
“UNTOLD STORIES OF EVERYDAY ADVERSITY & PERSEVERANCE”

Spotify: https://listen.brovamedia.net/show/7QP2k4RtwnLxHvBzMPYA9D?ref=pf3Wq8LmZc-Y52KdTrvehN

Target Market(s)

Podcast learning community

Industry/Entity Type

Podcast, Education

Colors
EB3D1F
EC4F4E
F09395
F8D3D4
FCEDEE

Requirements
Must have
• JV Logo, Colors are red, black and white.

```html
<!DOCTYPE html>
<html lang="en">
<head>
<meta charset="utf-8">
<title>The Quiet Ledger — Podcast Cover</title>
<link href="https://fonts.googleapis.com/css2?family=Montserrat:wght@300;600;800&display=swap" rel="stylesheet">
<style>
  :root {
    --red: #EB3D1F;
    --coral: #EC4F4E;
    --rose: #F09395;
    --blush: #F8D3D4;
    --petal: #FCEDEE;
    --ink: #0c0c0c;
    --badge: #1a1a1a;
    --white: #ffffff;
  }
  * { margin: 0; padding: 0; box-sizing: border-box; }
  html, body { width: 1200px; height: 1200px; overflow: hidden; background: var(--ink); }
  .cover {
    position: relative;
    width: 1200px;
    height: 1200px;
    overflow: hidden;
    font-family: "Montserrat", sans-serif;
    background: radial-gradient(circle at 78% 22%, #3a0d0c 0%, #140707 40%, var(--ink) 70%);
  }
  .cover-art { position: absolute; inset: 0; }
  .host-mark {
    position: absolute;
    left: 44px; top: 38px;
    color: var(--white);
    text-align: center;
    width: 140px;
  }
  .host-mark__initials { font-weight: 300; font-size: 76px; line-height: 1; letter-spacing: 2px; }
  .host-mark__name { font-weight: 600; font-size: 15px; letter-spacing: 1.5px; margin-top: 8px; }
  .show-title {
    position: absolute;
    right: 60px; top: 60px;
    width: 560px;
    text-align: right;
    color: var(--coral);
    font-weight: 600;
    font-size: 104px;
    line-height: 0.98;
    letter-spacing: 2px;
    text-transform: uppercase;
  }
  .host-credit {
    position: absolute;
    right: 60px; top: 520px;
    text-align: right;
    color: var(--white);
  }
  .host-credit__with { font-weight: 300; font-size: 30px; letter-spacing: 3px; }
  .host-credit__name { font-weight: 800; font-size: 38px; margin-top: 10px; }
  .listen-badge {
    position: absolute;
    right: 46px;
    width: 264px; height: 86px;
    border-radius: 12px;
    background: var(--badge);
    border: 2px solid #3a3a3a;
  }
  .listen-badge--first { top: 652px; }
  .listen-badge--second { top: 752px; }
  .tagline {
    position: absolute;
    left: 0; right: 0; top: 1030px;
    text-align: center;
    color: var(--white);
    font-weight: 800;
    font-size: 33px;
    line-height: 1.45;
    letter-spacing: 1.5px;
  }
</style>
</head>
<body>
<main class="cover">
  <svg class="cover-art" width="1200" height="1200" viewBox="0 0 1200 1200">
    <defs>
      <linearGradient id="portraitTone" x1="0" y1="0" x2="1" y2="1">
        <stop offset="0" stop-color="#6a6a6a"/>
        <stop offset="0.5" stop-color="#3e3e3e"/>
        <stop offset="1" stop-color="#242424"/>
      </linearGradient>
    </defs>
    <g role="img" aria-label="Black-and-white portrait of the host in a grey blazer over a white T-shirt, smiling">
      <path d="M0,1200 L0,540 C60,490 150,470 190,440 L190,170 C190,70 440,70 440,170 L455,440 C540,480 830,510 880,570 L910,1200 Z" fill="url(#portraitTone)"/>
    </g>
    <circle class="corner-disc" cx="70" cy="50" r="215" fill="var(--coral)"/>
    <polygon class="torn-edge" fill="var(--petal)"
      points="0,890 60,902 130,886 200,904 260,880 330,889 400,870 450,880 520,860 600,866 660,845 720,858 780,836 840,852 900,830 960,838 1020,820 1080,832 1140,810 1200,816 1200,1200 0,1200"/>
    <polygon class="torn-band" fill="var(--coral)"
      points="0,905 60,915 130,900 200,918 260,895 330,902 400,885 450,893 520,875 600,880 660,860 720,872 780,850 840,866 900,845 960,852 1020,836 1080,846 1140,826 1200,832 1200,1200 0,1200"/>
  </svg>

  <div class="host-mark">
    <div class="host-mark__initials">JV</div>
    <div class="host-mark__name">MARCUS ODELL</div>
  </div>

  <h1 class="show-title">The Quiet Ledger</h1>

  <div class="host-credit">
    <div class="host-credit__with">with :</div>
    <div class="host-credit__name">Marcus Odell</div>
  </div>

  <div class="listen-badge listen-badge--first" aria-label="Listening platform badge"></div>
  <div class="listen-badge listen-badge--second" aria-label="Listening platform badge"></div>

  <p class="tagline">“ UNTOLD STORIES OF<br>EVERYDAY ADVERSITY &amp; PERSEVERANCE “</p>
</main>
</body>
</html>
```